Non-governmental organisation branding design

We are looking to get the branding for our new NGO:

Tavelin Bridgework Centre

Our tag-line is: Peace through dialogue

We are a peace brokering organisation that conducts research and offers peace brokering services relating to conflicts around the world.

The branding needs to be simple, to the point and serious.

Other comparable organisations are:

https://www.qorvanhub.example/

http://zrt.example/

https://www.outerlumen.example/

Any questions, please get in touch.

Tavelin Bridgework Centre

1 page

```html
<!DOCTYPE html>
<html lang="en">
<head>
<meta charset="utf-8">
<title>Tavelin Bridgework Centre</title>
<link rel="stylesheet" href="https://fonts.googleapis.com/css2?family=Raleway:wght@300;400;500;600;700;800&family=Open+Sans:wght@400;600;700&display=swap">
<style>
:root{
  --red:#d42229;
  --red-dark:#b91c22;
  --ink:#333333;
  --muted:#555555;
  --grey-bg:#f4f4f4;
  --black:#000000;
  --white:#ffffff;
  --gold:#c9a04a;
}
*{box-sizing:border-box;margin:0;padding:0}
html,body{width:1200px;height:2363px;overflow:hidden}
body{position:relative;background:var(--white);font-family:'Raleway',sans-serif;color:var(--ink)}
.abs{position:absolute}

/* header */
.site-header{position:absolute;left:0;top:0;width:1200px;height:75px;background:var(--white)}
.brand{position:absolute;left:134px;top:20px;display:flex;align-items:center;gap:10px}
.brand-mark{width:34px;height:34px;border:3px solid var(--red);border-radius:50%}
.brand-name{font-family:'Raleway',sans-serif;font-weight:700;font-size:15px;line-height:17px;color:var(--red);width:130px}
.main-nav{position:absolute;right:132px;top:35px;display:flex;gap:28px}
.main-nav a{font-size:11.5px;font-weight:600;color:#444;text-decoration:none;letter-spacing:.3px}

/* hero */
.hero{position:absolute;left:0;top:75px;width:1200px;height:413px}
.hero-photo{position:absolute;inset:0;background:linear-gradient(180deg,#8f8a90 0%,#b9a7a0 38%,#d6c3aa 55%,#7a6a55 78%,#4a4232 100%)}
.hero-glow{position:absolute;left:720px;top:20px;width:320px;height:220px;border-radius:50%;background:radial-gradient(circle,rgba(255,250,235,.9),rgba(255,240,210,0) 70%)}
.hero-arrow{position:absolute;left:100px;top:180px;width:16px;height:34px}
.hero-title{position:absolute;left:144px;top:122px;width:480px;font-weight:800;font-size:22.5px;line-height:28px;color:var(--white);text-transform:uppercase}
.hero-lede{position:absolute;left:146px;top:193px;width:380px;font-size:12.5px;line-height:19px;color:var(--white)}
.btn-red{position:absolute;left:148px;top:264px;width:124px;height:33px;background:var(--red);color:var(--white);font-size:12px;display:flex;align-items:center;justify-content:center}

/* what we do */
.what-we-do{position:absolute;left:0;top:488px;width:1200px;height:467px}
.section-title{font-weight:400;font-size:23px;letter-spacing:.5px;color:#444}
.what-we-do .section-title{position:absolute;left:142px;top:64px}
.rule-gold{position:absolute;width:46px;height:2px;background:var(--gold)}
.what-we-do .rule-gold{left:146px;top:100px}
.body-copy{position:absolute;left:144px;top:118px;width:406px;font-size:10.3px;line-height:20px;color:#555}
.btn-outline{position:absolute;left:142px;top:376px;width:116px;height:32px;border:1px solid var(--red);border-radius:16px;color:var(--red);font-size:10.5px;display:flex;align-items:center;justify-content:center;letter-spacing:.4px}
.photo{position:absolute;border:5px solid var(--white)}
.photo-a{left:790px;top:66px;width:280px;height:224px;border:none;background:linear-gradient(135deg,#c8c7c2,#8b8a7e 55%,#4d5560)}
.photo-b{left:624px;top:186px;width:200px;height:136px;background:linear-gradient(135deg,#6d6a62,#a79c8a 50%,#3c3a36)}
.photo-c{left:788px;top:254px;width:204px;height:138px;background:linear-gradient(135deg,#8b7b6a,#514a44 50%,#c9bfb3)}

/* where we work */
.where-we-work{position:absolute;left:0;top:955px;width:1200px;height:439px;background:var(--red)}
.where-we-work .heading{position:absolute;left:143px;top:75px;font-weight:700;font-size:17.5px;color:var(--white);letter-spacing:.3px}
.where-we-work .rule-gold{left:145px;top:101px;width:30px}
.region-list{position:absolute;left:144px;top:118px;width:132px;list-style:none}
.region-list li{height:40.5px;border-bottom:1px solid rgba(255,255,255,.35);display:flex;align-items:center;justify-content:space-between;font-size:11px;font-weight:700;color:var(--white)}
.region-list li:last-child{border-bottom:none}
.region-list li span{font-size:8px}
.world-map{position:absolute;left:354px;top:60px;width:752px;height:310px;border-radius:40px 60px 80px 30px;background:linear-gradient(100deg,#f4d20a 0%,#f4d20a 30%,#f39419 48%,#2f8a5a 52%,#e83b95 68%,#a8141c 80%,#e21f8e 100%);opacity:.95}
.map-label{position:absolute;font-size:9.5px;color:var(--white);letter-spacing:.3px}
.map-label::after{content:"";display:block;width:18px;height:1px;background:var(--white);margin-top:3px}

/* latest news */
.latest-news{position:absolute;left:0;top:1394px;width:1200px;height:474px;background:var(--grey-bg)}
.latest-news .heading{position:absolute;left:0;top:58px;width:1200px;text-align:center;font-weight:700;font-size:18px;color:#333;letter-spacing:.3px}
.news-card{position:absolute;top:115px;width:294px}
.news-image{position:relative;height:166px}
.date-badge{position:absolute;right:10px;top:0;width:36px;height:39px;background:var(--red);color:var(--white);font-family:'Open Sans',sans-serif;font-size:10px;line-height:12px;text-align:center;padding-top:6px}
.date-badge b{display:block;font-weight:700}
.news-title{margin-top:12px;font-family:'Open Sans',sans-serif;font-weight:700;font-size:14px;color:#333}
.news-meta{margin-top:8px;font-family:'Open Sans',sans-serif;font-size:10px;line-height:19px;color:#444}
.overlay{position:absolute;inset:0;background:rgba(212,34,41,.78)}
.btn-ghost{position:absolute;left:84px;top:66px;width:110px;height:34px;border:1px solid rgba(255,255,255,.8);color:var(--white);font-size:10.5px;display:flex;align-items:center;justify-content:center}
.slider-dots{position:absolute;left:577px;top:428px;display:flex;gap:14px}
.slider-dots i{display:block;width:9px;height:9px;background:#ccc}
.slider-dots i.on{background:var(--red)}

/* newsletter */
.newsletter{position:absolute;left:0;top:1868px;width:1200px;height:200px;background:var(--red)}
.newsletter .heading{position:absolute;left:0;top:42px;width:1200px;text-align:center;font-weight:700;font-size:18px;color:var(--white);letter-spacing:.3px}
.newsletter .rule{position:absolute;left:574px;top:69px;width:52px;height:2px;background:var(--white)}
.field{position:absolute;top:109px;width:206px;height:40px;background:var(--white);font-size:11px;color:#bbb;padding:12px 14px}
.btn-signup{position:absolute;left:769px;top:109px;width:92px;height:40px;background:var(--black);color:var(--white);font-weight:700;font-size:11.5px;display:flex;align-items:center;justify-content:center}

/* footer */
.site-footer{position:absolute;left:0;top:2068px;width:1200px;height:295px;background:var(--black);color:var(--white)}
.site-footer .brand{left:141px;top:64px}
.address{position:absolute;left:148px;top:122px;font-size:11.5px;line-height:25px;color:var(--white)}
.divider-v{position:absolute;top:65px;width:1px;height:126px;background:#444}
.footer-links{position:absolute;left:388px;top:57px;list-style:none}
.footer-links li{font-size:11.5px;line-height:28px}
.footer-nav{position:absolute;left:628px;top:68px;width:440px;display:flex;flex-wrap:wrap;column-gap:30px;row-gap:26px}
.footer-nav span{font-size:10.5px;letter-spacing:.3px}
.divider-h{position:absolute;left:627px;top:148px;width:441px;height:1px;background:#444}
.social{position:absolute;left:629px;top:176px;display:flex;gap:18px}
.social i{display:block;width:15px;height:15px;border-radius:50%;background:#bbb}
.footer-rule{position:absolute;left:133px;top:239px;width:935px;height:1px;background:#333}
.copyright{position:absolute;left:137px;top:259px;font-size:8.5px;color:#ccc}
</style>
</head>
<body>

<header class="site-header">
  <div class="brand"><span class="brand-mark"></span><span class="brand-name">Tavelin Bridgework Centre</span></div>
  <nav class="main-nav">
    <a>WHO WE ARE</a><a>WHERE WE WORK</a><a>WHAT WE DO</a><a>GET INVOLVED</a><a>NEWS &amp; PRESS</a><a>RESOURCES</a>
  </nav>
</header>

<section class="hero">
  <div class="hero-photo" role="img" aria-label="Photo of people walking across a plain toward mountains at sunset"></div>
  <div class="hero-glow"></div>
  <svg class="hero-arrow" viewBox="0 0 16 34"><polyline points="14,2 2,17 14,32" fill="none" stroke="rgba(255,255,255,.7)" stroke-width="2"/></svg>
  <h1 class="hero-title">Are the U.S. and the Taliban finally ready for direct talks?</h1>
  <p class="hero-lede">With growing momentum, U.S. policy shift could be a critical step toward peace in Afghanistan</p>
  <div class="btn-red">Read More</div>
</section>

<section class="what-we-do">
  <h2 class="section-title">WHAT WE DO</h2>
  <div class="rule-gold"></div>
  <p class="body-copy">Lorem ipsum dolor sit amet, consectetuer adipiscing elit. Aenean commodo ligula eget dolor. Aenean massa. Cum sociis natoque penatibus et magnis dis parturient montes, nascetur ridiculus mus. Donec quam felis, ultricies nec, pellentesque eu, pretium quis, sem. Nulla consequat massa quis enim. Donec pede justo, fringilla vel, aliquet nec, vulputate eget, arcu. In enim justo, rhoncus ut, imperdiet a, venenatis vitae, justo. Nullam dictum felis eu pede mollis pretium. Integer tincidunt. Cras dapibus. Vivamus elementum semper nisi. Aenean vulputate eleifend tellus. Aenean leo ligula, porttitor eu, consequat vitae, eleifend ac, enim. Aliquam lorem ante, dapibus in, viverra quis, feugiat a, tellus. Phasellus viverra nulla ut metus varius laoreet. Quisque rutrum. Aenean imperdiet. Etiam ultricies nisi vel augue. Curabitur ullamcorper ultricies nisi. Nam eget dui. Etiam rhoncus. Maecenas tempus.</p>
  <div class="btn-outline">READ MORE</div>
  <div class="photo photo-a" role="img" aria-label="Photo of a field team meeting with local people"></div>
  <div class="photo photo-b" role="img" aria-label="Photo of a speaker addressing a workshop"></div>
  <div class="photo photo-c" role="img" aria-label="Photo of delegates seated at a hearing table"></div>
</section>

<section class="where-we-work">
  <h2 class="heading">WHERE WE WORK</h2>
  <div class="rule-gold"></div>
  <ul class="region-list">
    <li>Africa<span>&#9656;</span></li>
    <li>Asia<span>&#9656;</span></li>
    <li>Europe<span>&#9656;</span></li>
    <li>Middle East<span>&#9656;</span></li>
    <li>View All Regions<span>&#9656;</span></li>
  </ul>
  <div class="world-map" role="img" aria-label="World map with regions coloured: Americas yellow, Africa orange, Europe blue, Middle East green, Asia pink and red"></div>
  <span class="map-label" style="left:598px;top:130px">EUROPE</span>
  <span class="map-label" style="left:1003px;top:190px">ASIA</span>
  <span class="map-label" style="left:809px;top:255px">MIDDLE EAST</span>
  <span class="map-label" style="left:651px;top:296px">AFRICA</span>
  <span class="map-label" style="left:415px;top:313px">AMERICAS</span>
</section>

<section class="latest-news">
  <h2 class="heading">LATEST NEWS</h2>
  <article class="news-card" style="left:134px">
    <div class="news-image" role="img" aria-label="Photo of a swimmer resting at the pool edge" style="background:linear-gradient(180deg,#4fa3d6,#8cc9e8 60%,#d9eef7)">
      <div class="date-badge">July<b>10</b></div>
    </div>
    <h3 class="news-title">Brindle Outdoor Pool</h3>
    <p class="news-meta">Jul 26, 5:30 PM – 7:30 PM, Brindle Outdoor Pool, 220 Elm Row, Harwick, CO 80599, USA. Bring the whole fam for an evening at Brindle Pool!</p>
  </article>
  <article class="news-card" style="left:453px">
    <div class="news-image" role="img" aria-label="Photo of volunteers cleaning up a school yard" style="background:linear-gradient(135deg,#8a6b55,#c9a78a)">
      <div class="overlay"></div>
      <div class="date-badge">June<b>23</b></div>
      <div class="btn-ghost">Register Now</div>
    </div>
    <h3 class="news-title">School Cleanup</h3>
    <p class="news-meta">Location is TBD Jul 28, 5:00 PM – 6:00 PM<br>Location is TBD Join us to help clean up a local school!</p>
  </article>
  <article class="news-card" style="left:779px">
    <div class="news-image" role="img" aria-label="Photo of students gathered around a wooden play pit" style="background:linear-gradient(180deg,#6f8a4e,#8d8a6a 50%,#b59a6e)">
      <div class="date-badge">June<b>05</b></div>
    </div>
    <h3 class="news-title">Building Gaga Pit for Local School</h3>
    <p class="news-meta">Jul 14, 9:00 AM – 1:00 PM, Harwick Grammar School, 48 Quarry Way, Harwick, CO 80598, USA Help build a gaga - pit for Harwick Grammar</p>
  </article>
  <div class="slider-dots"><i></i><i class="on"></i><i></i></div>
</section>

<section class="newsletter">
  <h2 class="heading">NEWSLETTER</h2>
  <div class="rule"></div>
  <div class="field" style="left:292px">Name</div>
  <div class="field" style="left:528px">E-Mail ID</div>
  <div class="btn-signup">SIGNUP</div>
</section>

<footer class="site-footer">
  <div class="brand"><span class="brand-mark"></span><span class="brand-name">Tavelin Bridgework Centre</span></div>
  <p class="address">Marrow Lane, 410276 in<br>District 04.<br>Tel: +1 555.014.2283</p>
  <div class="divider-v" style="left:344px"></div>
  <ul class="footer-links">
    <li>Experts</li><li>Regions</li><li>Issue Areas</li><li>Education &amp; Training</li><li>Events</li>
  </ul>
  <div class="divider-v" style="left:576px"></div>
  <div class="footer-nav">
    <span>WHO WE ARE</span><span>WHERE WE WORK</span><span>WHAT WE DO</span><span>GET INVOLVED</span><span>NEWS &amp; PRESS</span><span>RESOURCES</span>
  </div>
  <div class="divider-h"></div>
  <div class="social"><i></i><i></i><i></i><i></i></div>
  <div class="footer-rule"></div>
  <p class="copyright">© Copyrights tavelinbridgework.example. All rights Reserved</p>
</footer>

</body>
</html>
```